Email Marketing Design for Airport Parking Website

Our company is doing a new email marketing campaign and we need a graphic designer to provide us with a template to use for these emails. We want a look that will grab the attention of the viewer. We're thinking some cartoonish art or photography oriented design with bright colors. We need it to be tasteful and appealing to business travelers as that is the target demographic for the campaign.

I have a mockup of the layout that we want. My hope is that I can provide the mockup and let the designer take it and run with it.

Target Market(s)

Business travelers and individuals who love to travel.

Industry/Entity Type

Graphic Designer

Requirements
Must have
• It must have all the elements in the mockup. It needs to be eye catching. The headline text a the top really needs to POP.

Also the completed format must be something I can slice up easily. It should be a layered PSD file. I will be using CSS3 so rounded corners and drop shadows are encouraged.

```html
<!DOCTYPE html>
<html lang="en">
<head>
<meta charset="utf-8">
<title>Harborline Parking Coupon Email</title>
<link href="https://fonts.googleapis.com/css2?family=Arimo:wght@400;700&display=swap" rel="stylesheet">
<style>
  :root {
    --brand-blue: #2a7db8;
    --button-blue: #3498db;
    --strip-dark: #34495e;
    --card-bg: #f3f3f3;
    --card-border: #3a3a3a;
    --text-dark: #333333;
    --offer-red: #e74c3c;
    --white: #ffffff;
    --logo-navy: #14284b;
  }
  * { margin: 0; padding: 0; box-sizing: border-box; }
  html, body { width: 1200px; height: 900px; overflow: hidden; background: var(--white); }
  body { position: relative; font-family: "Arimo", Arial, sans-serif; color: #000; }

  .site-header {
    position: absolute; left: 0; top: 0; width: 1200px; height: 100px;
    background: var(--brand-blue);
    display: flex; align-items: center; justify-content: center;
  }
  .site-header h1 {
    color: var(--white); font-size: 29px; font-weight: 700;
    text-shadow: 0 2px 3px rgba(0,0,0,.55); margin-top: -2px;
  }
  .thanks-strip {
    position: absolute; left: 0; top: 100px; width: 1200px; height: 27px;
    background: var(--strip-dark);
    border-top: 2px solid #5fa8dc; border-bottom: 2px solid #5fa8dc;
    color: var(--white); font-size: 18px; font-weight: 700;
    text-align: center; line-height: 23px;
  }
  .hero-art {
    position: absolute; left: 0; top: 127px; width: 1200px; height: 398px;
    background:
      radial-gradient(ellipse at 50% 95%, #4fe6f5 0%, rgba(79,230,245,0) 45%),
      linear-gradient(100deg, #5ab2e2 0%, #3bbde6 30%, #6fa6da 55%, #40c4e8 80%, #5a9fdc 100%);
  }
  .coupon {
    position: absolute; left: 300px; top: 183px; width: 601px; height: 286px;
    background: var(--card-bg); border: 1px solid var(--card-border);
    border-radius: 10px; box-shadow: 0 3px 8px rgba(0,0,0,.35);
    color: var(--text-dark);
  }
  .coupon-lead { position: absolute; left: 0; width: 420px; top: 17px; text-align: center; font-size: 23px; font-weight: 700; }
  .coupon-offer {
    position: absolute; left: 0; width: 420px; top: 52px; text-align: center;
    font-size: 62px; font-weight: 700; color: var(--offer-red);
    text-shadow: 0 3px 4px rgba(0,0,0,.35);
  }
  .coupon-terms { position: absolute; left: 20px; width: 380px; top: 137px; text-align: center; }
  .coupon-terms strong { display: block; font-size: 18px; }
  .coupon-terms p { font-size: 14px; line-height: 17px; }
  .coupon-warning { position: absolute; left: 0; width: 420px; top: 216px; text-align: center; font-size: 18px; font-weight: 700; }
  .coupon-fine { position: absolute; left: 25px; width: 550px; top: 250px; text-align: center; font-size: 9px; line-height: 12px; }
  .facility-logo { position: absolute; left: 434px; top: 62px; display: flex; align-items: center; gap: 12px; }
  .facility-logo .mark { width: 60px; height: 60px; background: var(--text-dark); }
  .facility-logo span { font-size: 18px; font-weight: 700; line-height: 22px; }
  .facility-address { position: absolute; left: 420px; width: 180px; top: 151px; text-align: center; font-size: 12px; line-height: 15px; }

  .reminder { position: absolute; left: 340px; width: 520px; top: 538px; text-align: center; font-size: 12px; font-weight: 700; line-height: 14px; }
  .rate-button {
    position: absolute; left: 419px; top: 589px; width: 362px; height: 42px;
    background: var(--button-blue); color: var(--white); font-size: 23px; font-weight: 700;
    display: flex; align-items: center; justify-content: center; text-decoration: none;
    box-shadow: 0 1px 3px rgba(0,0,0,.45);
  }
  .company-logo {
    position: absolute; left: 489px; top: 644px; width: 222px; height: 92px;
    border: 1px solid #222; background: #f2f2f2;
    display: flex; align-items: center; justify-content: center; gap: 10px;
  }
  .company-logo .mark { width: 22px; height: 22px; background: var(--logo-navy); }
  .company-logo span { font-size: 22px; font-weight: 700; color: var(--logo-navy); }
  .social-links {
    position: absolute; left: 509px; top: 759px; width: 182px; height: 42px;
    display: flex; box-shadow: 0 1px 3px rgba(0,0,0,.4);
  }
  .social-links a {
    flex: 1; background: var(--button-blue); color: var(--white); text-decoration: none;
    font-size: 13px; font-weight: 700; display: flex; align-items: center; justify-content: center;
    border-right: 1px solid #2a7db8;
  }
  .social-links a:last-child { border-right: 0; }
  .copyright { position: absolute; left: 0; width: 1200px; top: 830px; text-align: center; font-size: 12px; }
  .site-footer {
    position: absolute; left: 0; top: 848px; width: 1200px; height: 52px;
    background: var(--brand-blue); border-top: 2px solid #5fa8dc;
    display: flex; align-items: center; justify-content: center;
  }
  .site-footer a { color: var(--white); font-size: 11px; font-weight: 700; text-decoration: none; }
</style>
</head>
<body>
  <header class="site-header">
    <h1>Thank you for parking at Harborline Parking Lakeview Airport!</h1>
  </header>
  <div class="thanks-strip">Please accept this discount coupon as our thanks for your repeat business.</div>

  <div class="hero-art" role="img" aria-label="Bright illustration of city towers, airplanes in flight and paint splashes over swirling blue stripes"></div>

  <section class="coupon">
    <div class="coupon-lead">Redeem This Coupon For</div>
    <div class="coupon-offer">$2 OFF*</div>
    <div class="coupon-terms">
      <strong>Your next parking stay of 3 or more days.</strong>
      <p>TO USE: Present coupon to parling attendent upon arrival at the parking facility along with the printed confirmation of your parking reservation.</p>
    </div>
    <div class="coupon-warning">COUPON Not valid without Reservation</div>
    <p class="coupon-fine">* Fine print here. Etiam posuere massa et diam iaculis lobortis. Integer vitae imperdiet mauris. Vestibulum viverra dui in mi laoreet, a dignissim turpis posuere. Nam ut ante ac lacus mollis vulputate mattis non est.</p>
    <div class="facility-logo"><div class="mark"></div><span>Facility<br>Logo</span></div>
    <address class="facility-address" style="font-style:normal">
      Harborline Parking Lakeview Airport<br>45 Runway Ave<br>Lakeview, CA 90000<br>1 800 555 0147
    </address>
  </section>

  <p class="reminder">Don't forget to chack StayParkHub.com for the latest rate at Harborline Parking Lakeview Airport and to reserve your parking early!</p>
  <a class="rate-button" href="#">Check our Discounted Rate</a>
  <div class="company-logo"><div class="mark"></div><span>Parkway Co.</span></div>
  <nav class="social-links">
    <a href="#">Share</a><a href="#">Post</a><a href="#">Follow</a>
  </nav>
  <p class="copyright">Copyright (C) 2013 StayParkHub.com</p>
  <footer class="site-footer"><a href="#">Click here to unsubscribe from this mailing list.</a></footer>
</body>
</html>
```